Would like a Northwest feel to the look, something NOT typical of what you would see on a typical Home Inspectors logo. Real estate cards all the same as well, and would like to stand out. Earthy, green, Northwest. Sadly a portrait seems to be a requirement (see the attached). I inspect residential homes for buyers and sellers.

Target Market(s)

Home Buyers and Sellers

Industry/Entity Type

Home Inspection

Contact Information for Business Card

See description
Note: The name Corvaneth is a Chinook word that means 'Friend'. Please do not associate the name with the Whale that shows up on 99% of google searches.

Logo Text

Corvaneth Home Inspections

Colors

Designer to choose colors to be used in the design.

Requirements
Must have
• Phone Num: 541-672-8153
• Address: 732 SW 219th Av Num 618
• Portland, Oregon 97388
• Email: glen@corvanethhomeinspection.example
• Website: www.CorvanethHomeInspection.example
• Additional Note: Need to add the Obravex logo (icon). It should be small and not the focus of the card. The logo can be found at Obravex.example
Nice to have
• I am open
Should not have
• Cant think of anything

```html
<!DOCTYPE html>
<html lang="en">
<head>
<meta charset="utf-8">
<title>Corvaneth Home Inspections – Business Card</title>
<link href="https://fonts.googleapis.com/css2?family=Source+Sans+3:wght@400;600&display=swap" rel="stylesheet">
<style>
  :root {
    --backdrop: #666666;
    --leaf-green: #9cc63c;
    --paper-white: #ffffff;
    --ink: #1c1c1c;
    --card-black: #0d0d0d;
    --card-black-glow: #2b2b2b;
    --photo-tone-light: #c9cbbf;
    --photo-tone-dark: #7d8270;
    --sprout-tone: #b9dc6e;
  }
  * { box-sizing: border-box; margin: 0; padding: 0; }
  html, body { width: 1200px; height: 900px; overflow: hidden; }
  body {
    background: var(--backdrop);
    font-family: "Source Sans 3", "Myriad Pro", sans-serif;
    position: relative;
  }
  .card {
    position: absolute;
    top: 306px;
    width: 439px;
    height: 272px;
    border-radius: 12px;
    overflow: hidden;
  }
  .card-front { left: 149px; background: var(--leaf-green); }
  .card-back {
    left: 609px;
    background: radial-gradient(ellipse at 50% 45%, var(--card-black-glow) 0%, var(--card-black) 70%);
  }
  .front-divider { position: absolute; inset: 0; }
  .portrait {
    position: absolute;
    left: 0; top: 30px;
    width: 176px; height: 242px;
    background: linear-gradient(180deg, var(--photo-tone-light) 0%, var(--photo-tone-dark) 100%);
    border-radius: 80px 80px 0 0;
  }
  .sprout {
    position: absolute;
    left: 128px; top: 8px;
    width: 92px; height: 86px;
    background: radial-gradient(ellipse at 50% 50%, var(--sprout-tone) 0%, rgba(185,220,110,0) 72%);
  }
  .contact {
    position: absolute;
    left: 200px; width: 232px;
    text-align: center;
    color: var(--ink);
  }
  .contact-name { top: 76px; }
  .person-name { font-weight: 600; font-size: 15.5px; line-height: 18px; }
  .person-role { font-size: 12px; line-height: 14px; }
  .contact-address { top: 140px; font-size: 12px; line-height: 16px; }
  .contact-lines { top: 182px; font-size: 11.5px; line-height: 16px; }
  .contact-lines li {
    list-style: none;
    display: flex;
    align-items: center;
    justify-content: center;
    gap: 5px;
    white-space: nowrap;
  }
  .contact-lines svg { width: 8px; height: 8px; fill: var(--ink); flex: none; }
  .brand {
    position: absolute;
    left: 0; right: 0; top: 70px;
    text-align: center;
    color: var(--leaf-green);
    font-weight: 400;
  }
  .brand-dot {
    display: block;
    width: 40px; height: 40px;
    margin: 0 auto 14px;
    border-radius: 50%;
    background: var(--leaf-green);
  }
  .brand-name { font-size: 35px; letter-spacing: 2px; line-height: 36px; text-transform: uppercase; }
  .brand-sub { font-size: 14px; letter-spacing: 3px; line-height: 20px; text-transform: uppercase; }
</style>
</head>
<body>
  <section class="card card-front">
    <svg class="front-divider" viewBox="0 0 439 272" aria-hidden="true">
      <path d="M0 0 H120 C185 60 200 170 178 272 H0 Z" fill="var(--paper-white)"/>
      <path d="M122 0 C188 62 204 170 184 272" fill="none" stroke="var(--paper-white)" stroke-width="3"/>
    </svg>
    <div class="portrait" role="img" aria-label="Portrait photo of the inspector"></div>
    <div class="sprout" role="img" aria-label="Leaf sprout illustration"></div>

    <div class="contact contact-name">
      <p class="person-name">Marcus Hale</p>
      <p class="person-role">Managing Director</p>
    </div>
    <div class="contact contact-address">
      <p>732 SW 219th Av Num 618</p>
      <p>Portland, Oregon 97388</p>
    </div>
    <ul class="contact contact-lines">
      <li><svg viewBox="0 0 10 10"><path d="M1 3 Q5 0 9 3 L8 5 L6 4 L6 3 Q5 2.6 4 3 L4 4 L2 5 Z M2 6 H8 V9 H2 Z"/></svg>541-672-8153</li>
      <li><svg viewBox="0 0 10 10"><path d="M0 2 H10 V8 H0 Z" /><path d="M0 2 L5 6 L10 2" stroke="#9cc63c" stroke-width="1" fill="none"/></svg>glen@corvanethhomeinspection.example</li>
      <li><svg viewBox="0 0 10 10"><circle cx="5" cy="5" r="5"/></svg>www.CorvanethHomeInspection.example</li>
    </ul>
  </section>

  <section class="card card-back">
    <div class="brand">
      <span class="brand-dot"></span>
      <p class="brand-name">Corvaneth</p>
      <p class="brand-sub">Home Inspections</p>
    </div>
  </section>
</body>
</html>
```